Verpackungen für Parfum-Proben
Besten Dank! Das Team ist begeistert - also bin ich es auch und wir freuen uns schon, unsere Parfum Proben in Zukunft in diesem tollen Design weitergeben zu können! Danke!
Zielgruppe
Hallo allerseits! Wir sind im Direktvertrieb in den Bereichen Parfum & Kosmetik tätig.
Aufgabenstellung
Für unsere Parfum-Proben benötige ich ein ansprechendes, modernes Design.
Das Design muss relativ neutral gehalten werden, da die Blister sowohl für Herren- als auch Damenproben verwendet werden.
Auf Vorder- und Rückseite soll unser Team-Logo (RiechRitter®) sichtbar sein (Vorderseite größer, Rückseite kleiner).
Auf der linken Innenseite sollte Plätz für einen netten Spruch (den ich mir noch überlege) sein.
Auf der Rückseite muss Platz (weißes / helles Feld) für einen Stempel und/oder Aufkleber (Kontaktdaten des Distributors) sein.
Unser Logo ist Lila - Das farbliche Design sollte dazu passen.
Bei Fragen, einfach Nachricht :)
Daten:
Endformat: 133 x 74 mm
Datenformat: 139 x 80 mm
1-teilig, gestanzt, genutet, einseitig geklebt geliefert
Bitte verwenden Sie für positive Schriftstärken mindestens 9pt (ca. 3,17mm) und bei negativen Schriftstärken mindestens 13pt (ca. 4,59mm).
Abmessungen / Druck- / Designvorlage, Logo, etc.: https://ablage-wolke.example/ordner/Xy7PkTr2#b8fnWq0LmZ4vRc1_hJ6tDa

```html
<!DOCTYPE html>
<html lang="de">
<head>
<meta charset="utf-8">
<title>RiechRitter – Probenblister Außen- und Innenseite</title>
<link rel="stylesheet" href="https://fonts.googleapis.com/css2?family=Tenor+Sans&display=swap">
<style>
  :root {
    --page-bg: #f6f5f7;
    --brand-purple: #5a2a86;
    --accent-magenta: #d6157c;
    --field-white: #ffffff;
    --marble-light: #ece5f6;
    --marble-mid: #cbbbe7;
    --marble-deep: #9f89cf;
    --panel-shadow: rgba(60, 40, 90, 0.25);
  }
  * { box-sizing: border-box; margin: 0; padding: 0; }
  html, body { width: 1200px; height: 600px; overflow: hidden; }
  body {
    background: var(--page-bg);
    font-family: "Tenor Sans", sans-serif;
    position: relative;
  }
  .sheet {
    position: absolute;
    top: 144px;
    width: 560px;
    height: 311px;
    box-shadow: 6px 8px 18px var(--panel-shadow);
    overflow: hidden;
  }
  .sheet--outside { left: 25px; }
  .sheet--inside { left: 615px; }
  .marble-surface { position: absolute; inset: 0; width: 100%; height: 100%; }
  .cut-guides { position: absolute; inset: 0; width: 100%; height: 100%; }
  .cut-guides line { stroke: var(--accent-magenta); stroke-width: 1; stroke-dasharray: 5 3; }
  .cut-guides text { fill: var(--accent-magenta); font-size: 10px; font-family: sans-serif; }

  .field { position: absolute; background: var(--field-white); }
  .brand-name { color: var(--brand-purple); letter-spacing: 0.06em; white-space: nowrap; }
  .brand-dot {
    display: inline-block; border-radius: 50%;
    background: var(--brand-purple); vertical-align: middle;
  }

  .logo-tab {
    left: 73px; top: 0; width: 106px; height: 95px;
    border-radius: 0 0 10px 10px;
    display: flex; flex-direction: column; align-items: center; justify-content: center; gap: 6px;
  }
  .logo-tab .brand-name { font-size: 12px; }
  .logo-tab .brand-dot { width: 12px; height: 12px; }

  .logo-card {
    left: 349px; top: 77px; width: 169px; height: 156px;
    border-radius: 12px;
    display: flex; flex-direction: column; align-items: center; justify-content: center; gap: 12px;
  }
  .logo-card .brand-name { font-size: 20px; }
  .logo-card .brand-dot { width: 22px; height: 22px; }

  .stamp-field { position: absolute; left: 18px; top: 155px; width: 193px; height: 136px; }
  .stamp-field svg { position: absolute; inset: 0; }
  .stamp-field__label {
    position: absolute; left: 22px; top: 74px;
    color: var(--accent-magenta); font-size: 15px; line-height: 21px; letter-spacing: 0.08em;
  }

  .slogan-field {
    left: 23px; top: 79px; width: 215px; height: 155px;
    border-radius: 10px; padding: 30px 0 0 20px;
    color: var(--brand-purple);
  }
  .slogan-field__title { font-size: 15px; letter-spacing: 0.08em; margin-bottom: 12px; }
  .slogan-field__body { font-size: 11px; line-height: 16px; letter-spacing: 0.06em; padding-left: 8px; }

  .spine-tab {
    left: 498px; top: 116px; width: 48px; height: 195px;
    border-radius: 10px 10px 0 0;
    display: flex; align-items: center; justify-content: center;
  }
  .spine-tab .brand-name {
    font-size: 20px; transform: rotate(-90deg);
    display: flex; align-items: center; gap: 8px;
  }
  .spine-tab .brand-dot { width: 12px; height: 12px; }
</style>
</head>
<body>
  <svg width="0" height="0" style="position:absolute">
    <defs>
      <radialGradient id="marbleTone" cx="45%" cy="45%" r="75%">
        <stop offset="0" stop-color="#d6c9ee"/>
        <stop offset="0.5" stop-color="#c4b2e4"/>
        <stop offset="0.8" stop-color="#e6ddf4"/>
        <stop offset="1" stop-color="#b7a2dc"/>
      </radialGradient>
    </defs>
  </svg>

  <!-- Außenseite -->
  <section class="sheet sheet--outside">
    <svg class="marble-surface" viewBox="0 0 560 311" preserveAspectRatio="none" role="img" aria-label="Lila Marmorpapier-Muster als Hintergrund">
      <rect width="560" height="311" fill="url(#marbleTone)"/>
    </svg>
    <svg class="cut-guides" viewBox="0 0 560 311">
      <line x1="223" y1="50" x2="282" y2="50"/><text x="238" y="53">✂</text>
      <line x1="223" y1="79" x2="282" y2="79"/>
      <line x1="198" y1="134" x2="304" y2="134"/><text x="272" y="137">✂</text>
      <line x1="198" y1="176" x2="307" y2="176"/>
      <line x1="223" y1="231" x2="282" y2="231"/><text x="228" y="234">✂</text>
      <line x1="223" y1="261" x2="282" y2="261"/>
    </svg>

    <div class="field logo-tab">
      <span class="brand-name">RiechRitter</span>
      <span class="brand-dot"></span>
    </div>

    <div class="field logo-card">
      <span class="brand-name">RiechRitter</span>
      <span class="brand-dot"></span>
    </div>

    <div class="stamp-field">
      <svg viewBox="0 0 193 136">
        <path d="M10 0 H170 Q176 0 176 6 V24 Q176 33 185 33 H187 Q193 33 193 40 V128 Q193 136 185 136 H8 Q0 136 0 128 V10 Q0 0 10 0 Z" fill="#ffffff"/>
      </svg>
      <p class="stamp-field__label">Platz fur Angaben<br>oder Stempel</p>
    </div>
  </section>

  <!-- Innenseite -->
  <section class="sheet sheet--inside">
    <svg class="marble-surface" viewBox="0 0 560 311" preserveAspectRatio="none" role="img" aria-label="Lila Marmorpapier-Muster als Hintergrund">
      <rect width="560" height="311" fill="url(#marbleTone)"/>
    </svg>
    <svg class="cut-guides" viewBox="0 0 560 311">
      <line x1="278" y1="51" x2="337" y2="51"/><text x="312" y="54">✂</text>
      <line x1="278" y1="80" x2="337" y2="80"/>
      <line x1="252" y1="135" x2="362" y2="135"/><text x="266" y="138">✂</text>
      <line x1="252" y1="178" x2="362" y2="178"/>
      <line x1="278" y1="232" x2="337" y2="232"/><text x="320" y="235">✂</text>
      <line x1="278" y1="262" x2="337" y2="262"/>
    </svg>

    <div class="field slogan-field">
      <h2 class="slogan-field__title">Platz fur einen Slogan</h2>
      <p class="slogan-field__body">Platz fur Infotext. Platz fur<br>Infotext. Platz fur Infotext.<br>Platz fur Infotext. Platz fur<br>Infotext. Platz fur Infotext.</p>
    </div>

    <div class="field spine-tab">
      <span class="brand-name"><span class="brand-dot"></span>RiechRitter</span>
    </div>
  </section>
</body>
</html>
```